Ad design for magazines to promote our Cloud Computing Consulting Company Branding

We need an advertisement design to promote our brand online and on printed magazines (full page). We are a cloud consulting company (products & services on the Cloud) and would like to create an ad that conveys confidence in our services.
Some of the ideas we would want to project are:
First Spanish consulting company specialized in Cloud Computing Technology and Services
We help you incorporate into your business the best Cloud Computing Solutions on the market to improve efficiency, reduce costs and increase competitiveness
Experts in:
• Cloud infrastructure modernization
• Digital Transformation, productivity and collaboration
• Cloud data management
• Advanced analytics
• Cloud application development
• Location Strategy
We are Vexora Sky Ally Summit and have recently achieved a Task Renewal Mastery Tier award
We are also partners of other leading technologies
We have a web page to be used as reference even though we are open to designs that differ from this style. www.brevantacloud.example
Target Market(s)
B2B Market Business to Business
Requirements
Must have
- Dimensions: 21x29.7 cm. (width by height) CMYK, 300 dpi, 3 millimeters of bleed and cut lines
Nice to have
- We would like an attractive image with not a lot of text (just about what is on the explanation), including the Ally Summit and Task Renewal badges.

```html
<!DOCTYPE html>
<html lang="en">
<head>
<meta charset="utf-8">
<title>Brevanta Cloud – Cloud Consulting Ad</title>
<link rel="stylesheet" href="https://fonts.googleapis.com/css2?family=Montserrat:wght@400;500;600;700;800&family=Open+Sans:wght@400;600&display=swap">
<style>
  :root{
    --navy:#06264a;
    --deep:#0b4a86;
    --sky:#1aa3e0;
    --brand-blue:#1b8fd6;
    --accent-red:#d8262f;
    --ink:#2d3540;
    --muted:#6c7682;
    --line:#d5dde6;
    --white:#ffffff;
    --faint:#eef2f6;
  }
  *{box-sizing:border-box;margin:0;padding:0}
  html,body{width:800px;height:1200px;overflow:hidden;background:var(--white)}
  .ad{position:relative;width:800px;height:1200px;overflow:hidden;background:var(--white);font-family:"Open Sans",Arial,sans-serif;color:var(--ink)}

  .hero{position:absolute;top:0;left:0;width:800px;height:500px;
    background:radial-gradient(ellipse 60% 70% at 50% 45%,#1f8fd0 0%,var(--deep) 45%,var(--navy) 100%)}
  .hero-curve{position:absolute;top:380px;left:0;width:800px;height:140px}

  .hero-art{position:absolute;top:50px;left:230px;width:340px;height:340px;border-radius:12px;
    background:linear-gradient(180deg,rgba(255,255,255,.95) 0%,rgba(235,245,252,.9) 38%,rgba(120,195,240,.55) 70%,rgba(40,130,210,0) 100%)}
  .logo{position:absolute;top:108px;left:0;width:800px;display:flex;justify-content:center;align-items:center;gap:10px}
  .logo-dot{width:22px;height:22px;border-radius:50%;background:var(--accent-red)}
  .logo-name{font-family:"Montserrat",Arial,sans-serif;font-weight:800;font-size:22px;letter-spacing:.5px;color:var(--accent-red);text-transform:uppercase}

  .headline{position:absolute;top:470px;left:0;width:800px;text-align:center;font-family:"Montserrat",Arial,sans-serif}
  .headline .kicker{color:var(--accent-red);font-weight:700;font-size:22px}
  .headline h1{color:var(--brand-blue);font-weight:700;font-size:33px;line-height:1.2;margin-top:6px}

  .intro{position:absolute;top:602px;left:110px;width:580px;text-align:center;font-size:13.5px;line-height:1.5;color:var(--ink)}

  .experts-pill{position:absolute;top:668px;left:100px;width:600px;height:32px;border-radius:16px;background:var(--brand-blue);
    color:var(--white);font-family:"Montserrat",Arial,sans-serif;font-weight:700;font-size:16px;letter-spacing:1px;display:flex;align-items:center;justify-content:center}

  .services{position:absolute;top:726px;left:110px;width:580px;list-style:none;display:grid;grid-template-columns:repeat(3,1fr);row-gap:26px;column-gap:20px}
  .service{display:flex;flex-direction:column;align-items:center;text-align:center}
  .service-icon{width:50px;height:50px;border:2px solid var(--brand-blue);border-radius:8px;display:flex;align-items:center;justify-content:center}
  .service-icon svg{width:30px;height:30px;stroke:var(--brand-blue);fill:none;stroke-width:2;stroke-linecap:round;stroke-linejoin:round}
  .service-label{margin-top:9px;font-size:13px;font-weight:600;line-height:1.3;color:var(--ink);min-height:34px}

  .divider{position:absolute;top:980px;left:100px;width:600px;height:1px;background:var(--line)}

  .badges{position:absolute;top:1012px;left:80px;display:flex;gap:18px;align-items:flex-end}
  .badge-partner{width:130px;height:60px;border:1px solid var(--line);border-radius:4px;background:var(--faint)}
  .badge-award{width:110px;height:110px;border:1px solid var(--line);border-radius:6px;background:var(--faint)}

  .status{position:absolute;top:1020px;left:410px;width:330px;font-family:"Montserrat",Arial,sans-serif;color:var(--muted);font-size:14px;line-height:1.45}
  .status strong{display:block;color:var(--brand-blue);font-weight:700;font-size:16px}
  .status .small{font-size:12px;margin-top:4px}

  .faint-mark{position:absolute;bottom:-60px;right:-60px;width:300px;height:240px;border-radius:50%;
    background:radial-gradient(ellipse at center,rgba(220,228,236,.8) 0%,rgba(238,242,246,0) 70%)}
</style>
</head>
<body>
<main class="ad">
  <section class="hero">
    <div class="hero-art" role="img" aria-label="Illustration of a white cloud with streams of binary data falling beneath it"></div>
    <div class="logo">
      <span class="logo-dot"></span>
      <span class="logo-name">Brevanta Cloud</span>
    </div>
  </section>
  <svg class="hero-curve" viewBox="0 0 800 140" preserveAspectRatio="none" aria-hidden="true">
    <path d="M0 140 V60 Q400 -40 800 60 V140 Z" fill="#ffffff"/>
  </svg>

  <header class="headline">
    <p class="kicker">First Spanish Consulting Company</p>
    <h1>Specialized In Cloud Computing<br>Technology And Services</h1>
  </header>

  <p class="intro">We help you incorporate into your business the best Cloud Computing Solutions on the<br>market to improve efficiency, reduce costs and increase competitiveness</p>

  <div class="experts-pill">EXPERTS IN</div>

  <ul class="services">
    <li class="service">
      <span class="service-icon"><svg viewBox="0 0 30 30"><ellipse cx="15" cy="7" rx="10" ry="4"/><path d="M5 7v16c0 2 4.5 4 10 4s10-2 10-4V7"/><path d="M5 15c0 2 4.5 4 10 4s10-2 10-4"/></svg></span>
      <span class="service-label">Cloud data<br>management</span>
    </li>
    <li class="service">
      <span class="service-icon"><svg viewBox="0 0 30 30"><path d="M8 20h15a5 5 0 0 0 0-10 7 7 0 0 0-13-1 5.5 5.5 0 0 0-2 11Z"/><path d="M10 24v3M15 24v3M20 24v3"/></svg></span>
      <span class="service-label">Cloud infrastructure<br>modernization</span>
    </li>
    <li class="service">
      <span class="service-icon"><svg viewBox="0 0 30 30"><circle cx="15" cy="6" r="3"/><circle cx="6" cy="24" r="3"/><circle cx="24" cy="24" r="3"/><path d="M13.5 8.5 7.5 21.5M16.5 8.5l6 13M9 24h12"/></svg></span>
      <span class="service-label">Digital Transformation,<br>productivity &amp; collaboration</span>
    </li>
    <li class="service">
      <span class="service-icon"><svg viewBox="0 0 30 30"><path d="M4 26h22"/><path d="M7 26V17M13 26V11M19 26V14M25 26V6"/></svg></span>
      <span class="service-label">Advanced analytics</span>
    </li>
    <li class="service">
      <span class="service-icon"><svg viewBox="0 0 30 30"><rect x="8" y="3" width="14" height="24" rx="2"/><path d="M13 23h4"/><path d="M12 10l-2 3 2 3M18 10l2 3-2 3"/></svg></span>
      <span class="service-label">Cloud application<br>development</span>
    </li>
    <li class="service">
      <span class="service-icon"><svg viewBox="0 0 30 30"><path d="M15 27s-8-8-8-14a8 8 0 0 1 16 0c0 6-8 14-8 14Z"/><circle cx="15" cy="13" r="3"/></svg></span>
      <span class="service-label">Location Strategy</span>
    </li>
  </ul>

  <div class="divider"></div>

  <div class="badges">
    <div class="badge-partner" role="img" aria-label="Vexora Sky Ally partner badge"></div>
    <div class="badge-award" role="img" aria-label="Task Renewal Mastery Tier award badge"></div>
  </div>

  <div class="faint-mark" role="img" aria-label="Faint decorative cloud shape"></div>

  <div class="status">
    We are
    <strong>Vexora Sky Ally Summit</strong>
    Recently We have achieved a
    <strong>Task Renewal Mastery Tier award</strong>
    <p class="small">We are also partners of other leading technologies</p>
  </div>
</main>
</body>
</html>
```